Kestrel Gardenworks Business Card

An eye catching, yet simple business card that includes;

1. our logo
2. office phone - 5083172946
3. email - kestrelgardenworks@mailbrook.com
4. website - www.kestrelgardenworks.com
5. instagram - @kestrelgardenworksnv

```html
<!DOCTYPE html>
<html lang="en">
<head>
<meta charset="utf-8">
<title>Kestrel Gardenworks Business Card</title>
<link href="https://fonts.googleapis.com/css2?family=Montserrat:wght@400;500;700;800&display=swap" rel="stylesheet">
<style>
  :root {
    --backdrop: #161616;
    --card: #232323;
    --card-deep: #1c1c1c;
    --copper: #b8692a;
    --ink-light: #f2f2f2;
    --ink-soft: #d9d9d9;
    --gloss: #3a3a3a;
  }
  * { box-sizing: border-box; margin: 0; padding: 0; }
  html, body {
    width: 1200px; height: 900px; overflow: hidden;
    background: var(--backdrop);
    font-family: "Montserrat", sans-serif;
  }
  .stage {
    width: 1200px; height: 900px;
    display: flex; flex-direction: column; align-items: center; justify-content: center; gap: 36px;
  }
  .card {
    position: relative;
    width: 700px; height: 380px;
    background: linear-gradient(135deg, var(--card) 0%, var(--card-deep) 100%);
    border-bottom: 6px solid var(--copper);
    box-shadow: 0 18px 40px rgba(0,0,0,.55);
    overflow: hidden;
  }

  /* Front */
  .front-brand {
    position: absolute; inset: 0;
    display: flex; align-items: center; justify-content: center; gap: 18px;
  }
  .front-brand .brand-dot {
    width: 22px; height: 22px; border-radius: 50%; background: var(--gloss);
  }
  .front-brand .brand-name {
    font-weight: 800; font-size: 46px; letter-spacing: 1px; color: var(--gloss);
  }

  /* Back */
  .back-layout { position: absolute; inset: 0; }
  .back-brand {
    position: absolute; left: 40px; top: 118px; width: 245px;
    display: flex; align-items: center; gap: 12px;
  }
  .back-brand .brand-dot {
    flex: none; width: 18px; height: 18px; border-radius: 50%; background: var(--copper);
  }
  .back-brand .brand-name {
    font-weight: 800; font-size: 30px; line-height: 1.08; color: var(--copper);
  }
  .divider {
    position: absolute; left: 302px; top: 94px; width: 2px; height: 140px; background: var(--copper);
  }
  .contact {
    position: absolute; left: 324px; top: 94px; width: 350px;
  }
  .person-name {
    font-weight: 700; font-size: 26px; letter-spacing: 1px; color: var(--copper);
    text-transform: uppercase; white-space: nowrap; line-height: 1.1;
  }
  .person-role {
    font-size: 16px; color: var(--ink-light); margin-top: 2px; margin-bottom: 16px;
  }
  .contact-line {
    display: flex; align-items: center; gap: 8px; white-space: nowrap;
    font-size: 15px; color: var(--ink-light); line-height: 1.5;
  }
  .contact-line svg { flex: none; width: 13px; height: 13px; }
  .social {
    position: absolute; left: 0; right: 0; bottom: 52px;
    display: flex; justify-content: center; align-items: center; gap: 8px;
    font-size: 16px; color: var(--ink-soft); padding-left: 60px;
  }
  .social .social-dot {
    width: 16px; height: 16px; border-radius: 50%; background: var(--copper);
  }
</style>
</head>
<body>
<main class="stage">
  <section class="card card-front">
    <div class="front-brand">
      <span class="brand-dot"></span>
      <span class="brand-name">Kestrel Gardenworks</span>
    </div>
  </section>

  <section class="card card-back">
    <div class="back-layout">
      <div class="back-brand">
        <span class="brand-dot"></span>
        <span class="brand-name">Kestrel Gardenworks</span>
      </div>
      <div class="divider"></div>
      <div class="contact">
        <p class="person-name">Marcus Tellwood</p>
        <p class="person-role">Director</p>
        <p class="contact-line">
          <svg viewBox="0 0 16 16"><path d="M4 1l3 3-2 2c1 2 3 4 5 5l2-2 3 3-2 2C7 14 2 9 2 3z" fill="#b8692a"/></svg>
          (508) 317 2946
        </p>
        <p class="contact-line">
          <svg viewBox="0 0 16 16"><rect x="1.5" y="3.5" width="13" height="9" fill="none" stroke="#b8692a" stroke-width="1.5"/><path d="M1.5 3.5l6.5 5 6.5-5" fill="none" stroke="#b8692a" stroke-width="1.5"/></svg>
          kestrelgardenworks@mailbrook.com
        </p>
        <p class="contact-line">
          <svg viewBox="0 0 16 16"><circle cx="8" cy="8" r="6.5" fill="none" stroke="#b8692a" stroke-width="1.5"/><ellipse cx="8" cy="8" rx="3" ry="6.5" fill="none" stroke="#b8692a" stroke-width="1.2"/><path d="M1.5 8h13" stroke="#b8692a" stroke-width="1.2"/></svg>
          www.kestrelgardenworks.com
        </p>
      </div>
      <p class="social"><span class="social-dot"></span>@kestrelgardenworksnv</p>
    </div>
  </section>
</main>
</body>
</html>
```